Business Card design for a company called Tallow Flame NI

I need a business card design for my oil fired boiler servicing company. I have a logo design already and Im just looking that incorporated into the business card design. card details; Tallow Flame NI
Oil Burner Servicing - Mid Ulster Area
Service Engineer - Owen Marsh
Mobile 07751364927
email - Tallow.Flame.NI@hearthmail.example
www.tallowflameni.example
I carry out Servicing, Commissioning, Fault Finding, Warranty Validation
Target Market(s)
home owners with oil fired central heating
Industry/Entity Type
Business
Contact Information for Business Card
Tallow Flame NI
Tell. 07751364927
Web: www.tallowflameni.example
email Tallow.Flame.NI@Hearthmail.Example
Servicing Fault Finding Commissioning Warranty Validation
Look and feel

```html
<!DOCTYPE html>
<html lang="en">
<head>
<meta charset="utf-8">
<title>Tallow Flame NI – Business Card</title>
<link rel="stylesheet" href="https://fonts.googleapis.com/css2?family=Didact+Gothic&display=swap">
<style>
  :root {
    --page-bg: #e6e4df;
    --card-bg: #fbfbf8;
    --brand-green: #4bb430;
    --faint-green: #e3efe0;
    --ink-grey: #6a6a6a;
    --card-shadow: rgba(0, 0, 0, 0.14);
  }
  * { margin: 0; padding: 0; box-sizing: border-box; }
  html, body {
    width: 1200px;
    height: 803px;
    overflow: hidden;
    background: var(--page-bg);
    font-family: "Didact Gothic", "Century Gothic", sans-serif;
  }
  .canvas {
    position: relative;
    width: 1200px;
    height: 803px;
    display: flex;
    align-items: center;
    justify-content: center;
  }
  .business-card {
    position: relative;
    width: 1000px;
    height: 572px;
    background: var(--card-bg);
    box-shadow: 0 10px 30px var(--card-shadow);
    overflow: hidden;
  }
  .backdrop-ring {
    position: absolute;
    right: 40px;
    top: 60px;
    width: 340px;
    height: 340px;
  }
  .brand {
    position: absolute;
    left: 64px;
    top: 112px;
  }
  .brand-row {
    display: flex;
    align-items: center;
    gap: 18px;
  }
  .brand-dot {
    width: 78px;
    height: 78px;
    border-radius: 50%;
    background: var(--brand-green);
    flex: none;
  }
  .brand-name {
    color: var(--brand-green);
    font-size: 50px;
    line-height: 1;
    letter-spacing: 0.5px;
  }
  .brand-tagline {
    margin: 6px 0 0 96px;
    color: var(--brand-green);
    font-size: 12.5px;
    letter-spacing: 1.6px;
    text-transform: uppercase;
  }
  .service-lines {
    position: absolute;
    left: 70px;
    top: 300px;
    color: var(--brand-green);
    font-size: 28px;
    line-height: 40px;
  }
  .contact-lines {
    position: absolute;
    left: 70px;
    top: 408px;
    color: var(--ink-grey);
    font-size: 27px;
    line-height: 44px;
    letter-spacing: 1.6px;
  }
</style>
</head>
<body>
<main class="canvas">
  <section class="business-card" aria-label="Tallow Flame NI business card">
    <svg class="backdrop-ring" viewBox="0 0 340 340" aria-hidden="true">
      <circle cx="170" cy="170" r="150" fill="none" stroke="var(--faint-green)" stroke-width="26"/>
    </svg>

    <header class="brand">
      <div class="brand-row">
        <span class="brand-dot" aria-hidden="true"></span>
        <h1 class="brand-name">Tallow Flame NI</h1>
      </div>
      <p class="brand-tagline">Oil Burner Servicing - Mid Ulster Area</p>
    </header>

    <div class="service-lines">
      <p class="service-area">Oil Burner Servicing - Mid Ulster Area</p>
      <p class="engineer">Service Engineer - Owen Marsh</p>
    </div>

    <div class="contact-lines">
      <p class="phone">Tell. 07751364927</p>
      <p class="website">Web: www.tallowflameni.example</p>
      <p class="email">email Tallow.Flame.NI@Hearthmail.Example</p>
    </div>
  </section>
</main>
</body>
</html>
```